Online Marketplace Startup for Community Facilities (Tovaroom)

A innovative, modern website design is required for a new startup called Tovaroom. Tovaroom will be an online marketplace for searching for and booking community facilities, such as schools facilities (sports grounds, halls, classrooms etc.), churches, hospitals and other community facilities.

The attached brief has been created to provide guidance on the structure and content required.

The web design shall feature a modern, innovative but user friendly interface similar style to other web start up pages:
www.hallquiver.co.uk
www.vendlark.com.au
www.artfennel.com.au

The web design shall be ‘wordpress’ compliant and allow for future functionality to be added and coded (e.g. animations, flash, blogs etc) and content to be editable.

The following brief has been created to provide guidance on the structure and content required.

An existing logo developed for Tovaroom shall be utilised and incorporated in the top left hand cover of the cover landing page (refer to attached logo designs).

Refer to attached 'Website brief' for more details on requirements.
Updates

Project Deadline Extended
Reason: I wish to grant an extension to the deadline to provide designers with more time to submit their designs.

Target Market(s)

TovaRoom will focus on building a customer network of both community facility owners (schools, hospitals, churches) and hirers (non-government organisations, community groups, event management companies, commercial businesses). Members of the general public will also be encouraged to book facilities for private functions.

Industry/Entity Type

Community

Coding

Coded - Design and coding required

Number of Pages Required

5+ page

Font styles to use
Sans Serif

Colors
3176b5
ffffff
85cae6
33a6d7

Requirements
Must have
• The web design shall feature a modern, innovative but user friendly interface similar style to other web start up pages:
• www.hallquiver.co.uk
• www.vendlark.com.au
• www.artfennel.com.au
• The web design shall be ‘wordpress’ compliant and allow for future functionality to be added and coded (e.g. animations, flash, blogs etc) and content to be editable.
• Refer to Project brief for other requirements
Nice to have
• Refer to Project brief
Should not have
• Refer to Project brief

```html
<!DOCTYPE html>
<html lang="en">
<head>
<meta charset="utf-8">
<title>TovaRoom – Community Facility Bookings</title>
<link href="https://fonts.googleapis.com/css2?family=PT+Sans:wght@400;700&family=PT+Serif&display=swap" rel="stylesheet">
<style>
  :root{
    --brand-navy:#1f3e72;
    --nav-text:#3b5d8f;
    --button-blue:#2d6bc2;
    --icon-blue:#7aadf5;
    --icon-ink:#1f3e72;
    --heading-dark:#333a44;
    --body-grey:#8a9099;
    --hero-ink:#2b2e38;
    --rule:#e6e8eb;
    --white:#ffffff;
  }
  *{box-sizing:border-box;margin:0;padding:0}
  html,body{width:1079px;height:1200px;overflow:hidden;background:var(--white)}
  body{position:relative;font-family:"PT Sans",Arial,sans-serif}

  .site-header{position:absolute;left:0;top:0;width:1079px;height:76px;border-bottom:3px solid #f1f2f4}
  .brand{position:absolute;left:70px;top:14px;display:flex;align-items:center;gap:12px}
  .brand-mark{width:40px;height:40px;border-radius:50%;background:var(--brand-navy)}
  .brand-name{font-size:42px;color:var(--brand-navy);line-height:1;font-weight:400}
  .main-nav{position:absolute;top:31px;left:470px;display:flex;gap:26px;font-size:13.5px;color:var(--nav-text)}
  .main-nav svg{margin-top:2px}

  .hero{position:absolute;left:0;top:79px;width:1079px;height:611px;overflow:hidden}
  .hero-art{position:absolute;inset:0;
    background:
      radial-gradient(ellipse 260px 200px at 380px 230px,rgba(214,110,170,.75),transparent 70%),
      radial-gradient(ellipse 240px 180px at 830px 420px,rgba(190,150,200,.7),transparent 70%),
      radial-gradient(ellipse 300px 200px at 560px 430px,rgba(170,180,220,.7),transparent 70%),
      radial-gradient(ellipse 360px 240px at 150px 450px,rgba(150,175,215,.6),transparent 70%),
      linear-gradient(180deg,#eceef0 0%,#c9cbd0 45%,#b9bcc6 100%)}
  .hero-title{position:absolute;left:0;width:100%;top:88px;text-align:center;font-family:"PT Serif",Georgia,serif;font-size:44px;line-height:61px;color:var(--brand-navy)}
  .hero-lede{position:absolute;left:170px;width:739px;top:227px;text-align:center;font-size:17.5px;font-weight:700;line-height:31px;color:var(--hero-ink)}
  .hero-cta{position:absolute;left:385px;top:339px;width:310px;height:61px;background:var(--button-blue);color:var(--white);font-size:19px;display:flex;align-items:center;justify-content:center;border-radius:2px}
  .slider-arrow{position:absolute;top:278px}
  .slider-dots{position:absolute;top:496px;left:493px;display:flex;gap:8px}
  .slider-dots span{width:17px;height:17px;border-radius:50%;background:#dcdde2;border:2px solid #f5f5f7}
  .slider-dots span.current{background:transparent;border-color:var(--white)}

  .process-title{position:absolute;top:779px;width:100%;text-align:center;font-size:25px;color:var(--heading-dark)}
  .process-intro{position:absolute;top:821px;left:150px;width:779px;text-align:center;font-size:18.5px;line-height:31px;color:var(--body-grey)}
  .step{position:absolute;top:931px;width:240px;text-align:center}
  .step-icon{width:98px;height:98px;border-radius:50%;background:var(--icon-blue);margin:0 auto;display:flex;align-items:center;justify-content:center}
  .step-name{margin-top:17px;font-size:17.5px;color:var(--heading-dark)}
  .step-text{margin-top:10px;font-size:14.5px;line-height:25.5px;color:var(--body-grey)}
  .connector{position:absolute;top:974px;display:flex;gap:13px}
  .connector span{width:15px;height:15px;border-radius:50%;background:var(--icon-blue)}
  .page-rule{position:absolute;left:0;top:1178px;width:1079px;height:2px;background:var(--rule)}
</style>
</head>
<body>
  <header class="site-header">
    <div class="brand"><span class="brand-mark"></span><span class="brand-name">TovaRoom</span></div>
    <nav class="main-nav">
      <span>About Us</span><span>How it Works?</span><span>Services</span><span>Packages</span><span>Why Us?</span><span>News</span><span>FAQ</span>
      <svg width="16" height="12" viewBox="0 0 16 12"><rect x="0.5" y="0.5" width="15" height="11" fill="var(--nav-text)"/><path d="M1 1l7 6 7-6" stroke="#fff" stroke-width="1.4" fill="none"/></svg>
    </nav>
  </header>

  <section class="hero">
    <div class="hero-art" role="img" aria-label="Watercolour painting of pink and lilac peony flowers on a grey wash"></div>
    <h1 class="hero-title">THE TOVAROOM ONLINE PLATFORM<br>START-UP BUSINESS</h1>
    <p class="hero-lede">is a convenient and highly functional marketplace for searching and booking community facilities (schools, churches, health care facilities)</p>
    <div class="hero-cta">LET'S WORK TOGETHER</div>
    <svg class="slider-arrow" style="left:44px" width="56" height="56" viewBox="0 0 56 56"><circle cx="28" cy="28" r="26.5" fill="none" stroke="#6fa0ee" stroke-width="2"/><path d="M33 14L20 28l13 14" fill="none" stroke="#6fa0ee" stroke-width="2.5"/></svg>
    <svg class="slider-arrow" style="left:996px" width="56" height="56" viewBox="0 0 56 56"><circle cx="28" cy="28" r="26.5" fill="none" stroke="#6fa0ee" stroke-width="2"/><path d="M23 14l13 14-13 14" fill="none" stroke="#6fa0ee" stroke-width="2.5"/></svg>
    <div class="slider-dots"><span></span><span></span><span></span><span class="current"></span></div>
  </section>

  <h2 class="process-title">HOW DOES IT THE BOOKINGS PROCESS WORK?</h2>
  <p class="process-intro">Lorem ipsum dolor sit amet, consectetuer adipiscing elit. Donec odio. Quisque volutpat mattis eros.</p>

  <div class="step" style="left:66px">
    <div class="step-icon"><svg width="34" height="34" viewBox="0 0 34 34"><circle cx="13" cy="13" r="9" fill="none" stroke="var(--icon-ink)" stroke-width="4"/><path d="M20 20l10 10" stroke="var(--icon-ink)" stroke-width="5" stroke-linecap="round"/></svg></div>
    <div class="step-name">LOOKS FOR SPACE</div>
    <div class="step-text">advertised space / facility via TovaRoom online platform and makes application</div>
  </div>
  <div class="connector" style="left:268px"><span></span><span></span><span></span></div>

  <div class="step" style="left:295px">
    <div class="step-icon"><svg width="32" height="34" viewBox="0 0 32 34"><rect x="3" y="5" width="26" height="27" rx="2" fill="none" stroke="var(--icon-ink)" stroke-width="3"/><path d="M9 2v6M16 2v6M23 2v6M9 16h14M9 21h14M9 26h14" stroke="var(--icon-ink)" stroke-width="2.6"/></svg></div>
    <div class="step-name">APPLICATION</div>
    <div class="step-text">Evaluated by TovaRoom based on guidelines and criteria agreed with facility</div>
  </div>
  <div class="connector" style="left:502px"><span></span><span></span><span></span></div>

  <div class="step" style="left:537px">
    <div class="step-icon"><svg width="30" height="36" viewBox="0 0 30 36"><path d="M14 3a10 10 0 0 0-10 10c0 8 10 19 10 19s10-11 10-19A10 10 0 0 0 14 3z" fill="var(--icon-ink)"/><circle cx="14" cy="13" r="4" fill="var(--icon-blue)"/><path d="M16 27l4 4 8-9" fill="none" stroke="var(--icon-blue)" stroke-width="5"/><path d="M16 27l4 4 8-9" fill="none" stroke="var(--icon-ink)" stroke-width="2.5"/></svg></div>
    <div class="step-name">BOOKING</div>
    <div class="step-text">facility made via TovaRoom online bookings platform</div>
  </div>
  <div class="connector" style="left:738px"><span></span><span></span><span></span></div>

  <div class="step" style="left:772px">
    <div class="step-icon"><svg width="34" height="34" viewBox="0 0 34 34"><path d="M27 16v13H4V6h18" fill="none" stroke="var(--icon-ink)" stroke-width="3.5"/><path d="M10 15l6 6L31 5" fill="none" stroke="var(--icon-ink)" stroke-width="4"/></svg></div>
    <div class="step-name">INVOICE</div>
    <div class="step-text">generated and payment received prior to hire of facility</div>
  </div>

  <div class="page-rule"></div>
</body>
</html>
```